Business Cards and email stationery for VoiceOver Artist
Cutting Edge Business cards and email stationery for VoiceOver Artist
Use standard fonts
Not sure here?
Bright & Fun-filled
Marcus Dellow
Voiceover
2817 Palmera Ave
Encino CA 91427
(•••NO ADDRESS ON BUSINESS CARDS PLEASE••••)
818-555-2193 Cell
marcus@marcusdellow.example
marcusdellow.example
As 3-D as possible, cutting-edge, creative
1 Should be easy to read
2 Cell number should be listed first!
Uploaded Logo for VoiceOver Artist for Business cards and email Stationery
Logo for VoiceOver Artist v2

```html
<!DOCTYPE html>
<html lang="en">
<head>
<meta charset="utf-8">
<title>Marcus Dellow — Voiceover Business Card</title>
<link rel="stylesheet" href="https://fonts.googleapis.com/css2?family=Michroma&display=swap">
<style>
  :root {
    --page-bg: #e9e7e4;
    --card-dark: #3a3b3d;
    --card-dark-deep: #2c2d2f;
    --card-red: #e02a2f;
    --card-red-deep: #b5171c;
    --silver-light: #f2f2f2;
    --silver-mid: #a9abae;
    --text-light: #e6e6e6;
    --text-muted: #c9c9c9;
  }
  * { margin: 0; padding: 0; box-sizing: border-box; }
  html, body {
    width: 1200px;
    height: 914px;
    overflow: hidden;
    background: var(--page-bg);
  }
  .stage {
    position: relative;
    width: 1200px;
    height: 914px;
  }
  .business-card {
    position: absolute;
    left: 100px;
    top: 171px;
    width: 1000px;
    height: 572px;
    background: linear-gradient(160deg, var(--card-dark) 0%, var(--card-dark-deep) 100%);
    box-shadow: 0 14px 40px rgba(0,0,0,0.25);
    overflow: hidden;
    font-family: "Michroma", sans-serif;
    color: var(--text-light);
  }
  .card-art {
    position: absolute;
    inset: 0;
  }
  .identity {
    position: absolute;
    left: 58px;
    top: 48px;
  }
  .identity-name {
    font-size: 26px;
    font-variant: small-caps;
    letter-spacing: 1px;
    color: var(--text-light);
  }
  .identity-role {
    margin-top: 6px;
    font-size: 20px;
    font-variant: small-caps;
    letter-spacing: 1px;
    color: var(--text-muted);
  }
  .contact-list {
    position: absolute;
    left: 58px;
    top: 300px;
    list-style: none;
  }
  .contact-item {
    display: flex;
    align-items: center;
    gap: 10px;
    height: 28px;
    font-size: 15px;
    font-variant: small-caps;
    color: var(--text-light);
  }
  .contact-icon {
    width: 16px;
    height: 16px;
    flex: none;
  }
  .brand-lockup {
    position: absolute;
    left: 560px;
    top: 150px;
    width: 420px;
    display: flex;
    flex-direction: column;
    align-items: center;
    gap: 22px;
  }
  .brand-dot {
    width: 96px;
    height: 96px;
    border-radius: 50%;
    background: var(--silver-mid);
  }
  .brand-name {
    font-size: 34px;
    letter-spacing: 1px;
    color: var(--silver-light);
    text-transform: uppercase;
    white-space: nowrap;
  }
</style>
</head>
<body>
<main class="stage">
  <section class="business-card" aria-label="Business card for Marcus Dellow, Voiceover">
    <svg class="card-art" viewBox="0 0 1000 572" width="1000" height="572" aria-hidden="true">
      <defs>
        <linearGradient id="redPanel" x1="0" y1="0" x2="1" y2="1">
          <stop offset="0" stop-color="var(--card-red)"/>
          <stop offset="1" stop-color="var(--card-red-deep)"/>
        </linearGradient>
        <linearGradient id="silverBand" x1="0" y1="0" x2="0" y2="1">
          <stop offset="0" stop-color="var(--silver-light)"/>
          <stop offset="0.5" stop-color="var(--silver-mid)"/>
          <stop offset="1" stop-color="#6e7073"/>
        </linearGradient>
      </defs>
      <path d="M 530 0 C 440 50 390 250 380 572 L 400 572 C 412 260 460 60 555 0 Z" fill="url(#silverBand)"/>
      <path d="M 555 0 C 460 60 412 260 400 572 L 1000 572 L 1000 0 Z" fill="url(#redPanel)"/>
    </svg>

    <header class="identity">
      <h1 class="identity-name">Marcus Dellow</h1>
      <p class="identity-role">Voiceover</p>
    </header>

    <ul class="contact-list">
      <li class="contact-item">
        <svg class="contact-icon" viewBox="0 0 16 16" aria-hidden="true">
          <circle cx="8" cy="8" r="8" fill="var(--text-light)"/>
          <path d="M5 4.5 L6.5 4 L7.3 6 L6.4 6.8 C6.9 8 8 9.1 9.2 9.6 L10 8.7 L12 9.5 L11.5 11 C8 11 5 8 5 4.5 Z" fill="var(--card-dark)"/>
        </svg>
        <span>818-555-2193 Cell</span>
      </li>
      <li class="contact-item">
        <svg class="contact-icon" viewBox="0 0 16 16" aria-hidden="true">
          <circle cx="8" cy="8" r="8" fill="var(--text-light)"/>
          <rect x="4" y="5" width="8" height="6" fill="none" stroke="var(--card-dark)" stroke-width="1.2"/>
          <path d="M4 5 L8 8.5 L12 5" fill="none" stroke="var(--card-dark)" stroke-width="1.2"/>
        </svg>
        <span>marcus@marcusdellow.example</span>
      </li>
      <li class="contact-item">
        <svg class="contact-icon" viewBox="0 0 16 16" aria-hidden="true">
          <circle cx="8" cy="8" r="8" fill="var(--text-light)"/>
          <circle cx="8" cy="8" r="4.5" fill="none" stroke="var(--card-dark)" stroke-width="1.1"/>
          <ellipse cx="8" cy="8" rx="2" ry="4.5" fill="none" stroke="var(--card-dark)" stroke-width="1"/>
          <line x1="3.5" y1="8" x2="12.5" y2="8" stroke="var(--card-dark)" stroke-width="1"/>
        </svg>
        <span>www.marcusdellow.example</span>
      </li>
    </ul>

    <div class="brand-lockup">
      <div class="brand-dot" aria-hidden="true"></div>
      <p class="brand-name">Marcus Dellow</p>
    </div>
  </section>
</main>
</body>
</html>
```